New Business Card Design Project

Use the flyer uploaded and website www.brightoakbuilders.example for inspiration.
List Our Services on Backside of business cards
Marcus Dell
Harborline Renovations Inc.
Licensed General Contractors
555-014-7390

Contact Information for Business Card

Use the flyer uploaded and website www.brightoakbuilders.example for inspiration. List Our Services on Backside of business cards Marcus Dell Harborline Renovations Inc. Licensed General Contractors 555-014-7390

```html
<!DOCTYPE html>
<html lang="en">
<head>
<meta charset="utf-8">
<title>Harborline Renovations – Business Card</title>
<link href="https://fonts.googleapis.com/css2?family=Cinzel:wght@400;500&family=Arimo:wght@400&display=swap" rel="stylesheet">
<style>
  :root {
    --page-bg: #1b1b1c;
    --card-dark: #2b2b2d;
    --card-light: #ffffff;
    --ink-dark: #1e1e1e;
    --ink-muted: #7a7a7a;
    --ink-light: #f4f4f4;
  }
  * { margin: 0; padding: 0; box-sizing: border-box; }
  html, body { width: 1200px; height: 963px; overflow: hidden; background: var(--page-bg); }
  .canvas {
    width: 1200px; height: 963px;
    display: flex; flex-direction: column; align-items: center; justify-content: center;
    gap: 40px;
  }
  .card {
    position: relative;
    width: 760px; height: 434px;
    border-radius: 28px;
    overflow: hidden;
    box-shadow: 0 10px 30px rgba(0,0,0,.5);
  }

  /* Front */
  .card-front { background: var(--card-light); }
  .front-artwork { position: absolute; left: 0; top: 0; width: 330px; height: 434px; }
  .front-info { position: absolute; left: 360px; top: 150px; color: var(--ink-dark); }
  .brand-name {
    font-family: "Cinzel", serif; font-weight: 400;
    font-size: 30px; letter-spacing: 1px; text-transform: uppercase;
    color: var(--ink-dark);
  }
  .person-name {
    margin-top: 34px;
    font-family: "Cinzel", serif; font-weight: 400;
    font-size: 30px; letter-spacing: 1px; text-transform: uppercase;
  }
  .person-title {
    font-family: "Arimo", sans-serif; font-size: 20px; color: var(--ink-muted);
    margin-top: 4px;
  }
  .contact-list { list-style: none; margin-top: 26px; }
  .contact-list li {
    display: flex; align-items: center; gap: 12px;
    font-family: "Arimo", sans-serif; font-size: 19px; color: var(--ink-muted);
    margin-bottom: 10px;
  }
  .contact-list svg { width: 18px; height: 18px; flex: none; }

  /* Back */
  .card-back { background: var(--card-dark); color: var(--ink-light); }
  .services { position: absolute; left: 50px; top: 48px; }
  .services-heading {
    font-family: "Cinzel", serif; font-weight: 400;
    font-size: 30px; letter-spacing: 1px; text-transform: uppercase;
    margin-bottom: 14px;
  }
  .services-list { list-style: none; }
  .services-list li {
    display: flex; align-items: center; gap: 10px;
    font-family: "Arimo", sans-serif; font-size: 18px; line-height: 30px;
  }
  .services-list svg { width: 16px; height: 16px; flex: none; }
  .back-brand {
    position: absolute; right: 44px; top: 190px;
    font-family: "Cinzel", serif; font-weight: 400;
    font-size: 26px; letter-spacing: 1px; text-transform: uppercase;
    color: var(--ink-light);
  }
</style>
</head>
<body>
<main class="canvas">

  <section class="card card-front">
    <svg class="front-artwork" viewBox="0 0 330 434" role="img" aria-label="Large palm tree line illustration on dark background">
      <path d="M0 0 H330 C300 160 240 320 150 434 H0 Z" fill="var(--card-dark)"/>
    </svg>
    <div class="front-info">
      <div class="brand-name">Harborline Renovations</div>
      <div class="person-name">Marcus Dell</div>
      <div class="person-title">Licensed General Contractors</div>
      <ul class="contact-list">
        <li>
          <svg viewBox="0 0 24 24" fill="none" stroke="#333" stroke-width="2" stroke-linecap="round" stroke-linejoin="round"><path d="M22 16.9v3a2 2 0 0 1-2.2 2 19.8 19.8 0 0 1-8.6-3.1 19.5 19.5 0 0 1-6-6A19.8 19.8 0 0 1 2.1 4.2 2 2 0 0 1 4.1 2h3a2 2 0 0 1 2 1.7c.1 1 .4 1.9.7 2.8a2 2 0 0 1-.5 2.1L8 9.9a16 16 0 0 0 6 6l1.3-1.3a2 2 0 0 1 2.1-.4c.9.3 1.8.6 2.8.7a2 2 0 0 1 1.8 2z"/></svg>
          555-014-7390
        </li>
        <li>
          <svg viewBox="0 0 24 24" fill="none" stroke="#333" stroke-width="2"><circle cx="12" cy="12" r="10"/><path d="M2 12h20M12 2a15 15 0 0 1 0 20M12 2a15 15 0 0 0 0 20"/></svg>
          www.brightoakbuilders.example
        </li>
      </ul>
    </div>
  </section>

  <section class="card card-back">
    <div class="services">
      <h2 class="services-heading">Our Services</h2>
      <ul class="services-list">
        <li><svg viewBox="0 0 24 24" fill="none" stroke="currentColor" stroke-width="2.4"><circle cx="12" cy="12" r="10"/><path d="M7 12l3.5 3.5L17 9"/></svg>Remodel: Kitchen &amp; Bath</li>
        <li><svg viewBox="0 0 24 24" fill="none" stroke="currentColor" stroke-width="2.4"><circle cx="12" cy="12" r="10"/><path d="M7 12l3.5 3.5L17 9"/></svg>Painting: Interior &amp; Exterior</li>
        <li><svg viewBox="0 0 24 24" fill="none" stroke="currentColor" stroke-width="2.4"><circle cx="12" cy="12" r="10"/><path d="M7 12l3.5 3.5L17 9"/></svg>Flooring: Carpet, Vinyl, Wood</li>
        <li><svg viewBox="0 0 24 24" fill="none" stroke="currentColor" stroke-width="2.4"><circle cx="12" cy="12" r="10"/><path d="M7 12l3.5 3.5L17 9"/></svg>Window &amp; Door Replacement</li>
        <li><svg viewBox="0 0 24 24" fill="none" stroke="currentColor" stroke-width="2.4"><circle cx="12" cy="12" r="10"/><path d="M7 12l3.5 3.5L17 9"/></svg>Plumbing: Repairs &amp; Upgrades</li>
        <li><svg viewBox="0 0 24 24" fill="none" stroke="currentColor" stroke-width="2.4"><circle cx="12" cy="12" r="10"/><path d="M7 12l3.5 3.5L17 9"/></svg>Energy-Efficient Upgrades</li>
        <li><svg viewBox="0 0 24 24" fill="none" stroke="currentColor" stroke-width="2.4"><circle cx="12" cy="12" r="10"/><path d="M7 12l3.5 3.5L17 9"/></svg>Deck &amp; Patio Construction</li>
        <li><svg viewBox="0 0 24 24" fill="none" stroke="currentColor" stroke-width="2.4"><circle cx="12" cy="12" r="10"/><path d="M7 12l3.5 3.5L17 9"/></svg>Water &amp; Mold Damage</li>
        <li><svg viewBox="0 0 24 24" fill="none" stroke="currentColor" stroke-width="2.4"><circle cx="12" cy="12" r="10"/><path d="M7 12l3.5 3.5L17 9"/></svg>Garage Renovation</li>
      </ul>
    </div>
    <div class="back-brand">Harborline Renovations</div>
  </section>

</main>
</body>
</html>
```